I WAS JUST GIVING A SIZE THAT THE LABEL NEEDS TO BE ON OUR PACKAGING BAGS, IT IS 4X6. PLEASE MAKE SURE THAT DESIGN WILL FIT ON THAT SIZE.

We are looking to have you design the packaging for our coffee that will be sold online. The basics that we want on all the different varieties is our company name "Dunbarry's Gourmet Coffee & tagline " Gourmet Coffee for the Everyday Coffee Lover" and logo which is attached. If you ffind a different logo and want to change the colors in the logo, we are open to any suggestions. Our thoughts are travel the world with your coffee, that why we went with compass star. We are looking to use black bags for all as well. We would like a different picture background that is relatable to the type of coffee, if possible. The colors need to pop on the black bag. We need designs for the following flavors of coffee...

Brazilian Dark Roast
Columbian Supremo
100% Columbian Dark Roast
French Vanilla
Meadow Rhapsody
Kona Blend
Jamaican Blue Mountain Blend
Sumatra
Hazelnut
Irish Cream
Hawaiian Macadamia Nut Blend
Amaretto

All these flavors will be sold in 5# and 2# packages

```html
<!DOCTYPE html>
<html lang="en">
<head>
<meta charset="utf-8">
<title>Dunbarry's Gourmet Coffee – Brasilian Dark Roast</title>
<link rel="stylesheet" href="https://fonts.googleapis.com/css2?family=Alegreya+SC:wght@400;500&family=Roboto+Condensed:wght@400&family=Cormorant+Garamond:wght@500&display=swap">
<style>
  :root {
    --backdrop: #e4e4e4;
    --bag-black: #141414;
    --map-grey: #2e2e2e;
    --brand-white: #f1f1f1;
    --accent-green: #169a48;
    --band-green: #128a3f;
    --gold: #c9a44a;
    --web-grey: #4a4a4a;
  }
  * { box-sizing: border-box; margin: 0; padding: 0; }
  html, body {
    width: 800px;
    height: 1200px;
    overflow: hidden;
    background: var(--backdrop);
  }
  .canvas {
    position: relative;
    width: 800px;
    height: 1200px;
  }
  .label {
    position: absolute;
    left: 140px;
    top: 195px;
    width: 520px;
    height: 860px;
    background: var(--bag-black);
    color: var(--brand-white);
  }
  .world-map-area {
    position: absolute;
    left: 50px;
    top: 365px;
    width: 430px;
    height: 240px;
    background: radial-gradient(ellipse at center, var(--map-grey) 0%, rgba(46,46,46,0.5) 55%, rgba(20,20,20,0) 100%);
  }
  .brand-mark {
    position: absolute;
    left: 215px;
    top: 380px;
    width: 90px;
    height: 90px;
    border: 3px solid var(--gold);
    border-radius: 50%;
  }
  .brand-name {
    position: absolute;
    left: 0;
    top: 480px;
    width: 100%;
    text-align: center;
    font-family: "Alegreya SC", Georgia, serif;
    font-weight: 400;
    color: var(--brand-white);
    line-height: 1;
  }
  .brand-name .primary { display: block; font-size: 44px; letter-spacing: 1px; }
  .brand-name .secondary { display: block; font-size: 29px; letter-spacing: 2px; margin-top: 8px; line-height: 1.05; }
  .rule {
    position: absolute;
    left: 0;
    width: 100%;
    height: 3px;
    background: var(--accent-green);
  }
  .rule--band-top { top: 622px; }
  .rule--band-bottom { top: 682px; }
  .rule--weight-top { top: 782px; }
  .rule--weight-bottom { top: 826px; }
  .variety-band {
    position: absolute;
    left: 0;
    top: 630px;
    width: 100%;
    height: 44px;
    background: var(--band-green);
    display: flex;
    align-items: center;
    justify-content: center;
    font-family: "Alegreya SC", Georgia, serif;
    font-size: 23px;
    letter-spacing: 0.5px;
    color: var(--brand-white);
  }
  .tagline {
    position: absolute;
    left: 0;
    top: 712px;
    width: 100%;
    text-align: center;
    font-family: "Alegreya SC", Georgia, serif;
    font-size: 18px;
    line-height: 1.3;
    color: var(--brand-white);
  }
  .net-weight {
    position: absolute;
    left: 0;
    top: 797px;
    width: 100%;
    text-align: center;
    font-family: "Roboto Condensed", Arial, sans-serif;
    font-size: 14px;
    color: var(--brand-white);
  }
  .website {
    position: absolute;
    left: 0;
    top: 836px;
    width: 100%;
    text-align: center;
    font-family: "Cormorant Garamond", Georgia, serif;
    font-size: 13px;
    color: var(--web-grey);
  }
</style>
</head>
<body>
  <main class="canvas">
    <section class="label">
      <div class="world-map-area" role="img" aria-label="Faint world map background"></div>
      <span class="brand-mark" aria-hidden="true"></span>
      <h1 class="brand-name">
        <span class="primary">Dunbarry's</span>
        <span class="secondary">Gourmet<br>Coffee</span>
      </h1>
      <span class="rule rule--band-top"></span>
      <div class="variety-band">Brasilian Dark Roast</div>
      <span class="rule rule--band-bottom"></span>
      <p class="tagline">Gourmet Coffee for the<br>Everyday Coffee Lover</p>
      <span class="rule rule--weight-top"></span>
      <p class="net-weight">netto weight 5 oz</p>
      <span class="rule rule--weight-bottom"></span>
      <p class="website">www.dunbarrysgourmetcoffee.com</p>
    </section>
  </main>
</body>
</html>
```